Business Card, Stationary with Shark Logo for Personal Injury Lawyer

I need business cards and stationery with a shark logo for my Personal Injury Law Practice. Has to have this written on it:
Martin K. Hollis
Injury Lawyer
The Corvell Building
718 Tandy Street
Providence, Rhode Island 02908
401-627-4193
Martinhollis.com

Contact Information for Business Card

Martin K. Hollis, Injury Lawyer, address, 401-627-4193, martinhollis.com

```html
<!DOCTYPE html>
<html lang="en">
<head>
<meta charset="utf-8">
<title>Martin K. Hollis – Business Card</title>
<link href="https://fonts.googleapis.com/css2?family=Archivo:wght@400;900&display=swap" rel="stylesheet">
<style>
  :root {
    --navy: #2a2461;
    --navy-soft: #332d6d;
    --paper: #ffffff;
    --band: #e9e9f1;
    --ink: #1f1f24;
    --backdrop: #cfcfcf;
  }
  * { box-sizing: border-box; margin: 0; padding: 0; }
  html, body { width: 1200px; height: 900px; overflow: hidden; }
  body {
    background: var(--backdrop);
    font-family: "Archivo", Arial, sans-serif;
    position: relative;
  }
  .card {
    position: absolute;
    left: 320px;
    width: 560px;
    height: 320px;
    border-radius: 28px;
    overflow: hidden;
  }
  .card-front { top: 100px; background: var(--navy); }
  .card-back { top: 460px; background: var(--paper); }
  .card-band { position: absolute; inset: 0; }

  .brand {
    position: absolute;
    display: flex;
    align-items: center;
    gap: 14px;
  }
  .brand-mark { flex: none; }
  .brand-name {
    font-weight: 900;
    text-transform: uppercase;
    letter-spacing: 0.5px;
    line-height: 1;
    white-space: nowrap;
  }
  .card-front .brand {
    left: 0; right: 0; top: 138px;
    justify-content: center;
  }
  .card-front .brand-mark { width: 40px; height: 40px; background: var(--paper); }
  .card-front .brand-name { color: var(--paper); font-size: 40px; }

  .card-back .brand { left: 40px; top: 34px; }
  .card-back .brand-mark { width: 30px; height: 30px; background: var(--navy); }
  .card-back .brand-name { color: var(--navy); font-size: 30px; }

  .contact {
    position: absolute;
    left: 40px;
    top: 96px;
  }
  .contact-name {
    font-weight: 900;
    font-size: 20px;
    color: var(--navy);
    text-transform: uppercase;
    letter-spacing: 0.5px;
    line-height: 1.1;
  }
  .contact-role {
    font-size: 15px;
    color: var(--ink);
    margin-top: 2px;
    margin-bottom: 10px;
  }
  .contact-line {
    display: flex;
    align-items: center;
    gap: 10px;
    font-size: 15px;
    line-height: 1.3;
    color: var(--ink);
    margin-top: 6px;
  }
  .contact-line.is-address { align-items: flex-start; }
  .contact-line .accent { color: var(--navy); }
  .icon { width: 24px; height: 20px; flex: none; }
</style>
</head>
<body>
  <section class="card card-front">
    <svg class="card-band" viewBox="0 0 560 320" aria-hidden="true">
      <polygon points="380,0 560,0 560,320 430,320" fill="var(--navy-soft)"/>
    </svg>
    <div class="brand">
      <span class="brand-mark"></span>
      <span class="brand-name">Martin K. Hollis</span>
    </div>
  </section>

  <section class="card card-back">
    <svg class="card-band" viewBox="0 0 560 320" aria-hidden="true">
      <polygon points="390,0 560,0 560,320 445,320" fill="var(--band)"/>
    </svg>
    <div class="brand">
      <span class="brand-mark"></span>
      <span class="brand-name">Martin K. Hollis</span>
    </div>
    <div class="contact">
      <div class="contact-name">Martin K. Hollis</div>
      <div class="contact-role">Injury Lawyer</div>

      <div class="contact-line is-address">
        <svg class="icon" viewBox="0 0 24 20" aria-hidden="true">
          <rect width="24" height="20" fill="var(--navy)"/>
          <path d="M12 16 C8 11 7 9 7 7.5 A5 5 0 0 1 17 7.5 C17 9 16 11 12 16Z" fill="#fff"/>
          <circle cx="12" cy="7.5" r="1.8" fill="var(--navy)"/>
        </svg>
        <span>The Corvell Building, 718 Tandy Street<br>Providence, Rhode Island 02908</span>
      </div>
      <div class="contact-line">
        <svg class="icon" viewBox="0 0 24 20" aria-hidden="true">
          <rect width="24" height="20" fill="var(--navy)"/>
          <path d="M8 4 L10.5 4 L11.5 7.5 L10 8.8 C10.8 10.6 12.2 12 14 12.8 L15.3 11.3 L18.5 12.3 L18.5 15 C12 15.5 7 10.5 8 4Z" fill="#fff"/>
        </svg>
        <span>401-627-4193</span>
      </div>
      <div class="contact-line">
        <svg class="icon" viewBox="0 0 24 20" aria-hidden="true">
          <rect width="24" height="20" fill="var(--navy)"/>
          <rect x="4" y="5" width="16" height="10" fill="none" stroke="#fff" stroke-width="1.4"/>
          <polyline points="4,5 12,11 20,5" fill="none" stroke="#fff" stroke-width="1.4"/>
        </svg>
        <span>Martin@martinhollis.com</span>
      </div>
      <div class="contact-line">
        <svg class="icon" viewBox="0 0 24 20" aria-hidden="true">
          <rect width="24" height="20" fill="var(--navy)"/>
          <circle cx="12" cy="10" r="6.5" fill="none" stroke="#fff" stroke-width="1.3"/>
          <ellipse cx="12" cy="10" rx="2.8" ry="6.5" fill="none" stroke="#fff" stroke-width="1.1"/>
          <line x1="5.5" y1="10" x2="18.5" y2="10" stroke="#fff" stroke-width="1.1"/>
        </svg>
        <span>www.<span class="accent">Martinhollis</span>.com</span>
      </div>
    </div>
  </section>
</body>
</html>
```